Gaming Related Website

GuildWeave.com is a forum for gamers to connect online.

We would like a design for our front page.

Please feel free to include a basic logo.

Please take a look at the following sites for inspiration:
http://uk.plaryx.com/
http://eu.fraygrid.net/en/
http://www.stormvantor.com/

Target Market(s)

On-line gamers on consoles and PCs

Industry/Entity Type

Online

Requirements
Must have
• Please follow the wireframes attached.

```html
<!DOCTYPE html>
<html lang="en">
<head>
<meta charset="utf-8">
<title>GuildWeave.com – Headlines</title>
<link rel="stylesheet" href="https://fonts.googleapis.com/css2?family=Arimo:wght@400;700&display=swap">
<style>
:root{
  --blue:#2b609f;
  --blue-dark:#1f4d8a;
  --blue-light:#3a72b5;
  --link:#2c62a6;
  --panel:#dedede;
  --bar:#e4e4e4;
  --text:#333;
  --muted:#555;
  --white:#fff;
  --line:#9a9a9a;
}
*{box-sizing:border-box;margin:0;padding:0}
html,body{width:1200px;height:849px;overflow:hidden;background:var(--white)}
body{position:relative;font-family:"Arimo",Arial,sans-serif;color:var(--text)}
a{color:var(--link);text-decoration:none}

.site-header{position:absolute;left:0;top:0;width:1200px;height:92px;background:linear-gradient(#3166ab,#2a5d9d 60%,#24538f)}
.site-header::after{content:"";position:absolute;left:0;top:92px;width:1200px;height:6px;background:#d9d9d9}
.brand{position:absolute;left:40px;top:34px;font-size:25px;font-weight:700;color:#c9ccd3;letter-spacing:.5px}
.main-nav{position:absolute;left:315px;top:0;height:92px;display:flex}
.main-nav a{height:92px;display:flex;align-items:center;justify-content:center;text-align:center;color:var(--white);font-size:15px;line-height:18px;border-right:1px solid rgba(255,255,255,.35)}
.main-nav a.active{background:#e2e2e2;color:#111;border-right:none}
.main-nav a:last-child{border-right:1px solid rgba(255,255,255,.35)}

.profile{position:absolute;left:39px;top:98px;width:258px;height:178px;background:var(--panel)}
.avatar{position:absolute;left:14px;top:11px;width:93px;height:86px;background:linear-gradient(#f4f4f4,#e0c9a8 55%,#c98a1e);border:1px solid #c8c8c8}
.change-avatar{position:absolute;left:17px;top:101px;font-size:12px}
.user-name{position:absolute;left:125px;top:14px;font-size:15px;font-weight:700;color:#111}
.user-links{position:absolute;left:125px;top:38px;font-size:12px;color:var(--muted);word-spacing:38px}
.gaming-stats{position:absolute;left:125px;top:62px;font-size:15px}
.stats{position:absolute;left:18px;top:130px;display:flex;border:1px solid #b8b8b8;background:linear-gradient(#fff,#ececec);border-radius:3px}
.stat{height:38px;text-align:center;border-right:1px solid #b8b8b8;padding-top:3px}
.stat:last-child{border-right:none}
.stat b{display:block;font-size:17px;color:#111}
.stat span{font-size:9.5px;color:var(--muted)}

.games{position:absolute;left:39px;top:283px;width:258px;height:453px;background:var(--panel)}
.game-list{position:absolute;left:12px;top:15px;list-style:none}
.game-list li{width:217px;height:47px;margin-bottom:7px;background:linear-gradient(var(--blue-light),var(--blue-dark));border:2px solid #f2f2f2;outline:1px solid #9cb3d0;color:var(--white);font-size:15px;line-height:43px;padding-left:18px}
.scroll{position:absolute;width:4px;background:#bdbdbd}
.scroll i{position:absolute;left:-3px;width:10px;height:34px;background:#c9c9c9}

.tabs{position:absolute;display:flex;font-size:12.5px}
.tabs span{height:22px;line-height:22px;padding:0 9px;background:#e0e0e0;color:#222}
.tabs span.on{background:var(--blue);color:var(--white)}

.feed{position:absolute;left:315px;top:132px;width:607px;height:605px;border:1px solid var(--blue)}
.filter{height:39px;background:var(--bar);display:flex;align-items:center;padding-left:13px;font-size:12.5px;color:#333}
.filter b{margin-right:12px}
.filter label{display:flex;align-items:center;margin-right:11px}
.filter label::before{content:"";width:12px;height:12px;border:1px solid #bbb;background:#fff;margin-right:7px}
.feed-items{position:absolute;left:11px;top:40px;width:560px;font-size:14.5px;line-height:23px}
.actions{font-size:12.5px}
.feed .scroll{left:590px;top:64px;height:532px}

.side-box{position:absolute;left:941px;width:222px;border:1px solid var(--blue);font-size:12.5px}
.server{top:132px;height:272px}
.server-row{position:absolute;left:10px;display:flex;align-items:center}
.join{margin-left:8px;width:58px;height:20px;border:1px solid #aaa;background:linear-gradient(#fff,#e6e6e6);font-size:10px;text-align:center;line-height:18px;color:#333}
.box-link{position:absolute;left:13px;bottom:7px;font-size:11.5px}
.communities{top:460px;height:276px}
.community{position:absolute;left:13px;color:#333}

.site-footer{position:absolute;left:0;top:754px;width:1200px;height:95px;background:var(--blue)}
.site-footer p{position:absolute;top:45px;width:100%;text-align:center;font-size:9.5px;color:#e4ebf5}
</style>
</head>
<body>
<header class="site-header">
  <div class="brand">GuildWeave.com</div>
  <nav class="main-nav">
    <a class="active" style="width:101px">Headlines</a>
    <a style="width:74px">Forum</a>
    <a style="width:115px">Communities</a>
    <a style="width:107px">Challenges</a>
    <a style="width:135px">Games info and<br>Downloads</a>
    <a style="width:117px">Competitions</a>
    <a style="width:120px">Achievements</a>
    <a style="width:79px">Teams</a>
  </nav>
</header>

<section class="profile">
  <div class="avatar" role="img" aria-label="User avatar portrait"></div>
  <a class="change-avatar">Change Avatar</a>
  <div class="user-name">Lazy Gourmet</div>
  <div class="user-links">Edit Logout</div>
  <a class="gaming-stats">Gaming Stats</a>
  <div class="stats">
    <div class="stat" style="width:68px"><b>16</b><span>Games</span></div>
    <div class="stat" style="width:80px"><b>3</b><span>Communities</span></div>
    <div class="stat" style="width:68px"><b>2</b><span>Teams</span></div>
  </div>
</section>

<section class="games">
  <ul class="game-list">
    <li>All Games</li>
    <li>Distant Howl</li>
    <li>Edgewastes 2</li>
    <li>Veiled Blade III</li>
    <li>Line of Orders : Dark Ops 2</li>
    <li>Clan Strife 2</li>
    <li>Badge of Valor Frontline</li>
    <li>Realm of Embercraft</li>
  </ul>
  <div class="scroll" style="left:243px;top:15px;height:427px"><i style="top:108px"></i></div>
</section>

<div class="tabs" style="left:325px;top:109px"><span class="on">Newsfeed</span><span>Chats</span></div>
<section class="feed">
  <div class="filter">
    <b>Filter by :</b>
    <label>Notifications</label>
    <label>My Communities</label>
    <label>My Teams</label>
    <label>My Competitions</label>
  </div>
  <div class="feed-items">
    <p style="margin-top:22px">You have been challenged by Pokri for a 1v1 game of Tremor Arena at 12:30, Today</p>
    <p class="actions" style="margin-top:3px"><a>Accept</a> &nbsp;|&nbsp; <a>Decline</a></p>
    <p style="margin-top:56px">New patch is for Realm of Embercraft . <a>(Read More )</a></p>
    <p style="margin-top:11px">Mini has posted in the <b>Team Hot Shots</b> Private Board</p>
    <p style="margin-top:31px">You have been invited to join 50 Klicks gaming community <a>(Link)</a></p>
    <p class="actions" style="margin-top:13px"><a>Accept</a> &nbsp;|&nbsp; <a>Reject</a> &nbsp;|&nbsp; <a>Ignore</a></p>
    <p style="margin-top:55px">Lorem Ipsum is simply dummy text of the printing and typesetting industry.<br>Lorem Ipsum has been the industry's standard dummy text ever since the 1500s, when an unknown printer took a galley of type and scrambled it to make a type specimen book.</p>
    <p style="margin-top:23px">It has survived not only five centuries, but also the leap into electronic typesetting, remaining essentially unchanged.</p>
  </div>
  <div class="scroll"><i style="top:58px"></i></div>
</section>

<div class="tabs" style="left:972px;top:109px"><span class="on">Game Server</span><span>VOIP Channels</span></div>
<section class="side-box server">
  <div class="server-row" style="top:12px">Warfront 3.........32/18<span class="join">JOIN</span></div>
  <div class="server-row" style="top:48px">Warfront 3.........32/18<span class="join">JOIN</span></div>
  <div class="server-row" style="top:84px">Warfront 3.........32/18<span class="join">JOIN</span></div>
  <a class="box-link">Add a Game Srver</a>
</section>

<div class="tabs" style="left:972px;top:437px"><span class="on">My Communities</span><span>My Teams</span></div>
<section class="side-box communities">
  <div class="community" style="top:15px">PlayCircle.com.......8 Online</div>
  <div class="community" style="top:50px">PlayCircle.com.......8 Online</div>
  <div class="community" style="top:84px">PlayCircle.com.......8 Online</div>
  <div class="community" style="top:119px">PlayCircle.com.......8 Online</div>
  <div class="community" style="top:153px">PlayCircle.com.......8 Online</div>
  <a class="box-link">Set up a Community</a>
</section>

<footer class="site-footer">
  <p>List of Members, Filtered by game, Community, team or any combination of the three. For just games the system will show how many players are online</p>
</footer>
</body>
</html>
```